Brochure for Community-Based Therapy Company

Will be given out to patients, doctors, case managers. We are redesigning our marketing materials and would like a design for a brochure. We provide therapy to individuals who have been injured in car accidents or on the job. We provide occupational therapy, speech therapy and psychotherapy. We would like the brochure to utilize our corporate ID and color scheme that we are using for our other materials (see attached letterhead and logo).

Stock photos that are used should stay away from images of outpatient or hospital settings, stay away from photos with obvious disabilities (wheelchairs, learning to walk, etc), and nothing that looks like physical therapy, as we don't provide physical therapy only OT, Speech and psychotherapy. Would prefer to not have people wearing masks, as we will use this beyond the pandemic. Also, our staff wears business casual clothing so would prefer photos that the individuals are not wearing scrubs or other medical attire (lab coats, etc).

Target Market(s)

Patients, Physicians/Doctors, Case Managers

Industry/Entity Type

Healthcare

Requirements
Must have
• Prefer a booklet format but doesn't have to be 8.5 inch by 11 inch (can be a little smaller).

```html
<!DOCTYPE html>
<html lang="en">
<head>
<meta charset="utf-8">
<title>Community-Based Therapy Brochure Spread</title>
<link href="https://fonts.googleapis.com/css2?family=Jost:wght@400;500&family=Pathway+Gothic+One&display=swap" rel="stylesheet">
<style>
  :root{
    --paper:#ffffff;
    --ink:#1a1a1a;
    --body:#2b2b2b;
    --icon-line:#3a3a3a;
    --icon-ring:#8a8a8a;
    --mist-light:#f4f4f4;
    --mist-mid:#dedede;
    --mist-dark:#c9c9c9;
    --illus:#b9b9b9;
  }
  *{margin:0;padding:0;box-sizing:border-box}
  html,body{width:1200px;height:775px;overflow:hidden;background:var(--paper)}
  .spread{position:relative;width:1200px;height:775px;background:var(--paper);overflow:hidden;font-family:"Jost",sans-serif;color:var(--ink)}
  .family-photo{position:absolute;left:0;top:440px;width:1200px;height:335px;
    background:linear-gradient(180deg,rgba(255,255,255,0) 0%,var(--mist-light) 30%,var(--mist-mid) 70%,var(--mist-dark) 100%)}
  .garden-illustration{position:absolute;left:152px;top:44px;width:266px;height:187px;
    background:radial-gradient(ellipse at 55% 55%,var(--illus) 0%,#d6d6d6 55%,#efefef 100%);border-bottom:1px solid #444}
  .approach-title{position:absolute;left:127px;top:250px;font-size:25px;font-weight:400;line-height:30px;letter-spacing:.3px}
  .approach-copy{position:absolute;left:204px;top:325px;width:310px;font-size:8.9px;line-height:11.8px;color:var(--body)}
  .approach-copy p{margin-bottom:11.8px}
  .serve-title{position:absolute;left:705px;top:60px;font-size:24px;font-weight:400;letter-spacing:.3px}
  .serve-copy{position:absolute;left:711px;top:118px;width:360px;font-family:"Pathway Gothic One",sans-serif;font-size:11.3px;line-height:15px;color:var(--body)}
  .serve-copy p{margin-bottom:15px}
  .diagnosis{position:absolute;display:flex;align-items:center;gap:11px;font-size:9.2px;line-height:10.8px;text-transform:uppercase;letter-spacing:.2px}
  .diagnosis svg{flex:none;width:38px;height:38px}
  .funding{position:absolute;left:720px;top:620px;font-family:"Pathway Gothic One",sans-serif;font-size:11.3px;color:var(--body)}
  .funding ul{list-style:none;margin:10px 0 0 42px;font-family:"Jost",sans-serif;font-size:9.3px;line-height:16px;letter-spacing:.2px}
  .funding li::before{content:"• "}
</style>
</head>
<body>
<div class="spread">
  <div class="family-photo" role="img" aria-label="Soft grey photograph of a family walking hand in hand across a sunlit meadow"></div>

  <div class="garden-illustration" role="img" aria-label="Illustration of a gardener on a ladder watering flowers growing from a head, with a faint brain outline behind"></div>

  <h1 class="approach-title">WHY OUR APPROACH TO<br>BRAIN INJURY IS UNIQUE</h1>
  <div class="approach-copy">
    <p>In more traditional therapy settings such as programs using outpatient models, attempts are made to simulate functional activities, combined with more structured tasks, all performed within their clinic environment. However, the inability to generalize learning has been shown to be a reoccurring difficulty for individuals with Traumatic Brain Injury and can often manifest in cognitive inflexibility, which makes carryover of their learned skills to the real world, a challenge.</p>
    <p>Community-based treatment circumvents this difficulty by conducting therapy in the person’s home, school, workplace, or other settings within their community, such as a grocery store or at a post office. Clinicians are therefore able to witness first hand where a task is experiencing success or breaking down and can structure treatment accordingly. This allows for greater natural development of functional skills, with generalization issues no longer an obstacle toward meeting treatment goals.</p>
    <p>At Pathway Community Rehab we are committed to helping people recover their cognitive, physical and psychosocial abilities following brain injury through intensive individual treatment which focuses on safety, skill building and increasing independence, community reintegration, and overall life satisfaction. Our treatment approach is two-fold, with emphasis not only on direct restoration of brain functions, but also on helping the individual learn compensatory strategies (e.g., internal mnemonics, organizational systems, self-cuing techniques) or acquire assistive devices (e.g., planners, electronic reminders). Such methods are designed to reduce the effects of real-world disability when there is enduring cognitive impairment, and are most effective when introduced within a person’s own relevant environments.</p>
  </div>

  <h2 class="serve-title">WHAT WE SERVE</h2>
  <div class="serve-copy">
    <p>We treat adults and adolescents with a variety of diagnoses. We service home and community locations throughout Southeast and mid-Michigan.</p>
    <p>Our therapists hold a variety of certifications and endorsements including CBIS (Certified Brain Injury Specialist), SwallowCare, and VoiceBoost.</p>
    <p>Diagnoses can include:</p>
  </div>

  <svg width="0" height="0" style="position:absolute">
    <defs>
      <symbol id="ring" viewBox="0 0 38 38">
        <circle cx="19" cy="19" r="18" fill="#fff" stroke="var(--icon-ring)" stroke-width="1"/>
        <circle cx="19" cy="19" r="8" fill="none" stroke="var(--icon-line)" stroke-width="1.1"/>
      </symbol>
    </defs>
  </svg>

  <div class="diagnosis" style="left:731px;top:244px"><svg><use href="#ring"/></svg><span>Traumatic<br>brain injury</span></div>
  <div class="diagnosis" style="left:731px;top:292px"><svg><use href="#ring"/></svg><span>Spinal cord<br>injury</span></div>
  <div class="diagnosis" style="left:731px;top:340px"><svg><use href="#ring"/></svg><span>Depression</span></div>
  <div class="diagnosis" style="left:731px;top:387px"><svg><use href="#ring"/></svg><span>Mood<br>disorders</span></div>
  <div class="diagnosis" style="left:731px;top:434px"><svg><use href="#ring"/></svg><span>Visual<br>impairments</span></div>
  <div class="diagnosis" style="left:731px;top:482px"><svg><use href="#ring"/></svg><span>Movement<br>disorders</span></div>
  <div class="diagnosis" style="left:731px;top:530px"><svg><use href="#ring"/></svg><span>Dysphagia</span></div>

  <div class="diagnosis" style="left:928px;top:245px"><svg><use href="#ring"/></svg><span>Postconcussional<br>syndrome</span></div>
  <div class="diagnosis" style="left:928px;top:298px"><svg><use href="#ring"/></svg><span>Post-traumatic<br>stress disorder</span></div>
  <div class="diagnosis" style="left:928px;top:357px"><svg><use href="#ring"/></svg><span>Anxiety</span></div>
  <div class="diagnosis" style="left:928px;top:417px;gap:7px"><svg><use href="#ring"/></svg><span>Musculoskeletal/<br>orthopedic injuries<br><span style="text-transform:none">(ie. Spinal fractures/pathology,<br>nerve injuries, pain)</span></span></div>
  <div class="diagnosis" style="left:928px;top:473px"><svg><use href="#ring"/></svg><span>Balance<br>disorders</span></div>
  <div class="diagnosis" style="left:928px;top:531px"><svg><use href="#ring"/></svg><span>Neuromuscular<br>pathologies</span></div>

  <div class="funding">
    <p>Funding Sources include:</p>
    <ul>
      <li>NO-FAULT AUTO INSURANCE</li>
      <li>WORKERS COMPENSATION INSURANCE</li>
      <li>SOME COMMERCIAL HEALTH INSURANCE CARRIERS</li>
    </ul>
  </div>
</div>
</body>
</html>
```